Voltrix Power Flyer

Voltrix has developed a device that can properly align incoming electrical current into major energy usage facilities like hotels and hospitals. Designed in the UK, it has shown guaranteed energy savings of 7%. Now being introduced into the USA, our focus is on States that have highest energy costs like Hawaii, CA and NY. I am looking for design help with a 8.5X11 flyer that can be customized for each prospective hotel property client. Content will stay the same and once layout chosen, would like to be able to change the Picture of each prospective hotel site on front of flyer. All the info and basics of layout are established. Simply need some professional help to further design and make it print ready. Logo will need to be adjusted but basic design for that is established also.

```html
<!DOCTYPE html>
<html lang="en">
<head>
<meta charset="utf-8">
<title>Voltrix Power Flyer</title>
<link rel="stylesheet" href="https://fonts.googleapis.com/css2?family=Anton&family=Oswald:wght@500&family=Montserrat:wght@600;700;800&family=Poppins:wght@300;400;600;700&display=swap">
<style>
:root{
  --teal:#2a8a8f;
  --teal-dark:#0c3b40;
  --teal-deep:#0f4448;
  --cyan:#1bb3cf;
  --blue:#1ea0ff;
  --charcoal:#2a2a2c;
  --white:#ffffff;
  --ink:#1b1b1b;
  --stage:#e4e4e4;
  --cream:#f3efe0;
}
*{box-sizing:border-box;margin:0;padding:0}
html,body{width:963px;height:1200px;overflow:hidden;background:var(--stage)}
body{position:relative;font-family:'Poppins',sans-serif}
.page{position:absolute;top:306px;width:455px;height:588px;overflow:hidden;box-shadow:0 8px 20px rgba(0,0,0,.25)}
.page--back{left:18px;background:var(--white)}
.page--front{left:490px;background:var(--teal-deep)}
.abs{position:absolute}

/* back page */
.heading{font-family:'Montserrat',sans-serif;font-weight:700;color:var(--teal);font-size:12px;letter-spacing:.2px}
.heading small{font-size:9px}
.ticks{list-style:none;font-size:9.6px;color:var(--ink);line-height:11.6px}
.ticks li{display:flex;align-items:center;gap:6px}
.ticks svg{width:9px;height:9px;flex:none}
.brand{font-family:'Poppins',sans-serif;font-weight:700;letter-spacing:-1px}
.brand--back{left:336px;top:24px;font-size:36px;color:var(--ink);display:flex;align-items:center;gap:6px}
.brand--back .mark{width:14px;height:14px;background:var(--teal)}
.divider-v{left:271px;top:113px;width:1.5px;height:76px;background:var(--teal)}
.side{left:0;top:205px;width:172px;height:383px;background:linear-gradient(180deg,var(--teal-dark) 0%,#14545a 55%,var(--teal) 100%);color:var(--white);font-family:'Montserrat',sans-serif;padding:0 10px 0 28px}
.side h2{font-weight:800;font-size:21px;line-height:1.1}
.side p{font-weight:700;font-size:10.6px;line-height:13.2px}
.side hr{border:0;border-top:1px solid rgba(255,255,255,.6);margin:15px 0 14px}
.photo-site{left:172px;top:205px;width:283px;height:383px;background:linear-gradient(160deg,#8f9396 0%,#6f7376 50%,#555a5d 100%)}
.contact{left:177px;top:478px;width:269px;height:82px;background:rgba(240,240,240,.94);padding:7px 0 0 33px;font-family:'Montserrat',sans-serif}
.contact .label{color:var(--teal);font-weight:700;font-size:11px;line-height:12px}
.contact .name{font-weight:600;font-size:11.5px;color:var(--ink);border-bottom:1px solid var(--teal);display:inline-block;padding-right:14px;margin-bottom:5px}
.contact .row{display:flex;align-items:center;gap:8px;font-weight:600;color:var(--ink);line-height:17px}
.contact svg{width:11px;height:11px;flex:none}

/* front page */
.title{left:28px;top:24px;font-family:'Anton',sans-serif;font-size:60px;line-height:58px;letter-spacing:-.5px;background:linear-gradient(180deg,#7fd2ff 0%,var(--blue) 45%,#0a72d6 100%);-webkit-background-clip:text;background-clip:text;color:transparent}
.subband{left:0;top:168px;width:282px;height:22px;background:#1c6d72;color:var(--white);font-family:'Oswald',sans-serif;font-size:12.5px;line-height:22px;text-align:center;letter-spacing:.1px}
.energy-field{left:0;top:190px;width:282px;height:285px;background:radial-gradient(circle at 50% 55%,#7fd7ff 0%,#2ea7d6 35%,#1d7d86 70%,var(--teal) 100%)}
.hotel-photo{left:22px;top:221px;width:258px;height:258px;border-radius:50%;border:3px solid var(--white);background:linear-gradient(180deg,#1d4f8f 0%,#3d7cc0 40%,#d29a55 70%,#1b2f4d 100%)}
.column{left:282px;top:0;width:173px;height:475px;background:var(--charcoal);color:var(--white)}
.column .intro{position:absolute;left:11px;top:45px;width:150px;font-weight:300;font-size:11.4px;line-height:12.8px}
.rule{position:absolute;left:11px;width:152px;height:1px;background:rgba(255,255,255,.55)}
.promise{position:absolute;left:0;top:220px;width:173px;height:61px;background:var(--cyan);padding:4px 0 0 5px}
.promise .lead{font-size:10px;font-weight:300}
.promise .lead b{font-weight:700}
.promise .big{display:flex;align-items:center;gap:5px;margin-top:-1px}
.promise .pct{font-family:'Montserrat',sans-serif;font-weight:800;font-size:35px;line-height:36px}
.promise .caps{font-size:10.6px;line-height:11px;font-weight:400}
.note{position:absolute;left:11px;top:290px;width:150px;border-left:2px solid var(--teal);padding-left:5px;font-size:8.6px;line-height:10px;font-weight:300}
.facts{position:absolute;left:11px;top:357px;font-size:8px;line-height:9.4px;font-weight:300}
.facts b{font-weight:700;display:block}
.facts div{margin-bottom:6px}
.band-bottom{left:0;top:475px;width:455px;height:113px;background:var(--teal)}
.brand--front{left:26px;top:519px;font-size:36px;color:var(--cream);display:flex;align-items:center;gap:6px}
.brand--front .mark{width:14px;height:14px;background:var(--cream)}
.strip{left:141px;top:522px;width:314px;height:66px;background:var(--white);display:flex;align-items:center;padding-left:14px;font-family:'Poppins',sans-serif}
.strip .who{font-size:8px;color:var(--ink);font-weight:600;line-height:10px}
.strip .phone{display:flex;align-items:center;gap:4px;color:var(--teal);font-size:12.5px;font-weight:600}
.strip svg{width:10px;height:10px}
.strip .sep{width:1px;height:30px;background:var(--teal);margin:0 7px}
.strip .mail{text-align:center;color:var(--teal);font-size:8px;font-weight:600}
</style>
</head>
<body>

<section class="page page--back">
  <div class="abs heading" style="left:28px;top:38px">GUARANTEED PERFORMANCE</div>
  <ul class="abs ticks" style="left:28px;top:56px;line-height:15.5px">
    <li><svg viewBox="0 0 10 10"><path d="M1 5.5l2.5 2.5L9 1.5" fill="none" stroke="#2a8a8f" stroke-width="1.8"/></svg>Minimum 7% reduction (contractually backed)</li>
    <li><svg viewBox="0 0 10 10"><path d="M1 5.5l2.5 2.5L9 1.5" fill="none" stroke="#2a8a8f" stroke-width="1.8"/></svg>No operational changes required</li>
  </ul>
  <div class="abs brand brand--back">HRG<span class="mark"></span></div>

  <div class="abs heading" style="left:27px;top:106px">REAL-WORLD RESULTS <small>(UK HOTEL CASE)</small></div>
  <ul class="abs ticks" style="left:28px;top:125px">
    <li><svg viewBox="0 0 10 10"><path d="M1 5.5l2.5 2.5L9 1.5" fill="none" stroke="#2a8a8f" stroke-width="1.8"/></svg>11.2% reduction achieved</li>
    <li><svg viewBox="0 0 10 10"><path d="M1 5.5l2.5 2.5L9 1.5" fill="none" stroke="#2a8a8f" stroke-width="1.8"/></svg>32,954 kWh saved annually</li>
    <li><svg viewBox="0 0 10 10"><path d="M1 5.5l2.5 2.5L9 1.5" fill="none" stroke="#2a8a8f" stroke-width="1.8"/></svg>£7,579/year (~£630/month)</li>
    <li><svg viewBox="0 0 10 10"><path d="M1 5.5l2.5 2.5L9 1.5" fill="none" stroke="#2a8a8f" stroke-width="1.8"/></svg>6.4-month payback</li>
    <li><svg viewBox="0 0 10 10"><path d="M1 5.5l2.5 2.5L9 1.5" fill="none" stroke="#2a8a8f" stroke-width="1.8"/></svg>No disruption</li>
  </ul>
  <div class="abs divider-v"></div>
  <div class="abs heading" style="left:287px;top:106px">KEY BENEFITS</div>
  <ul class="abs ticks" style="left:287px;top:125px">
    <li><svg viewBox="0 0 10 10"><path d="M1 5.5l2.5 2.5L9 1.5" fill="none" stroke="#2a8a8f" stroke-width="1.8"/></svg>Zero CAPEX</li>
    <li><svg viewBox="0 0 10 10"><path d="M1 5.5l2.5 2.5L9 1.5" fill="none" stroke="#2a8a8f" stroke-width="1.8"/></svg>Day-one savings</li>
    <li><svg viewBox="0 0 10 10"><path d="M1 5.5l2.5 2.5L9 1.5" fill="none" stroke="#2a8a8f" stroke-width="1.8"/></svg>No disruption</li>
    <li><svg viewBox="0 0 10 10"><path d="M1 5.5l2.5 2.5L9 1.5" fill="none" stroke="#2a8a8f" stroke-width="1.8"/></svg>No maintenance</li>
    <li><svg viewBox="0 0 10 10"><path d="M1 5.5l2.5 2.5L9 1.5" fill="none" stroke="#2a8a8f" stroke-width="1.8"/></svg>Proven 7–11% performance</li>
  </ul>

  <div class="abs side">
    <h2 style="margin-top:26px">30 Day</h2>
    <p>No Obligation Trial Once approved to begin trial, Voltrix Flow Pro installed at no cost. Energy usage monitored immediately.</p>
    <hr>
    <h2>After Trial and Client Satisfied</h2>
    <p>After trial and energy savings realized, a 5 year lease agreement will be signed to continue service.</p>
  </div>
  <div class="abs photo-site" role="img" aria-label="Photo of the energy saving device installed on a grey electrical panel in a hotel plant room"></div>
  <div class="abs contact">
    <div class="label">CONTACT</div>
    <div class="name">Daniel Kealoha</div>
    <div class="row" style="font-size:12px"><svg viewBox="0 0 12 12"><path d="M2.5 1l2 2.2-1 1.3a6 6 0 0 0 3.4 3.4l1.3-1 2.2 2-1.3 1.6C5.5 10.5 1.5 6.5.9 2.3z" fill="#2a8a8f"/></svg>(808) 555-0147</div>
    <div class="row" style="font-size:11px"><svg viewBox="0 0 12 12"><rect x="1" y="2.5" width="10" height="7" fill="#2a8a8f"/><path d="M1 2.5l5 4 5-4" fill="none" stroke="#fff" stroke-width="1"/></svg>HRGservices808@example.com</div>
  </div>
</section>

<section class="page page--front">
  <div class="abs energy-field" role="img" aria-label="Electric blue lightning burst radiating around the hotel photo"></div>
  <div class="abs hotel-photo" role="img" aria-label="Photo of the prospective hotel property at dusk"></div>
  <h1 class="abs title">VOLTRIX<br>FLOWPRO</h1>
  <div class="abs subband">MAUI HOTEL ENERGY SAVINGS — ZERO CAPEX</div>

  <div class="abs column">
    <p class="intro">Guaranteed energy savings for maui resorts Maui hotels operate in one of the highest-cost energy environments in the united states. Even small efficiency gains translate into Major financial impact.</p>
    <div class="rule" style="top:204px"></div>
    <div class="promise">
      <div class="lead"><b>Voltrix FlowPro</b> delivers</div>
      <div class="big"><span class="pct">7%</span><span class="caps">ENERGY<br>SAVINGS<br>GUARANTEED</span></div>
    </div>
    <p class="note">with real-world results often exceeding 10% — without disrupting operations.</p>
    <div class="rule" style="top:335px"></div>
    <div class="facts">
      <div><b>THE OPPORTUNITY</b>(700-ROOM MAUI RESORT)</div>
      <div><b>Annual Energy Use:</b>~18–25M kWh</div>
      <div><b>Electric Cost:</b>$0.35–$0.45/kWh</div>
      <div><b>Annual Spend:</b>$6M – $11M</div>
    </div>
  </div>

  <div class="abs band-bottom"></div>
  <div class="abs brand brand--front">HRG<span class="mark"></span></div>
  <div class="abs strip">
    <div>
      <div class="who">Daniel Kealoha</div>
      <div class="phone"><svg viewBox="0 0 12 12"><path d="M2.5 1l2 2.2-1 1.3a6 6 0 0 0 3.4 3.4l1.3-1 2.2 2-1.3 1.6C5.5 10.5 1.5 6.5.9 2.3z" fill="#1b1b1b"/></svg>(808) 555-0147</div>
    </div>
    <div class="sep"></div>
    <div class="mail">
      <svg viewBox="0 0 12 12"><rect x="1" y="2.5" width="10" height="7" fill="#1b1b1b"/><path d="M1 2.5l5 4 5-4" fill="none" stroke="#fff" stroke-width="1"/></svg><br>HRGservices808@example.com
    </div>
  </div>
</section>

</body>
</html>
```